Velno Recycling needs a new web design

We need a new web design for our company based in Austin, TX. We resell and recycling electronics such as laptops, computer components, Tovlets, Brunos, etc. Since our inception over ten years ago, we’ve become one of the premier electronics recycling and remarketing companies in Austin, Texas.

```html
<!DOCTYPE html>
<html lang="en">
<head>
<meta charset="utf-8">
<title>Velno Recycling</title>
<link href="https://fonts.googleapis.com/css2?family=Roboto:wght@400;500;700;900&family=Open+Sans:wght@400;600&display=swap" rel="stylesheet">
<style>
:root{
  --blue:#1c6fc4;
  --blue-dark:#155aa3;
  --green:#2fb10f;
  --green-dark:#259209;
  --ink:#222;
  --text:#555;
  --dark:#262626;
  --darker:#1c1c1c;
  --light:#f1f1f1;
  --white:#fff;
}
*{box-sizing:border-box;margin:0;padding:0}
html,body{width:1200px;height:3896px;overflow:hidden}
body{position:relative;font-family:"Open Sans",Arial,sans-serif;color:var(--text);background:var(--white)}
h1,h2,h3,h4,.brand,.btn,.nav a{font-family:Roboto,Arial,sans-serif}
.section{position:absolute;left:0;width:1200px}
.btn{position:absolute;display:inline-flex;align-items:center;justify-content:center;height:34px;padding:0 20px;border-radius:17px;font-size:12px;font-weight:500;color:var(--white);text-decoration:none;white-space:nowrap}
.btn-blue{background:var(--blue)}
.btn-green{background:var(--green)}
.btn-white{background:var(--white);color:var(--ink)}
.ph{position:absolute}

/* header */
.header{top:0;height:83px;background:var(--white)}
.brand{position:absolute;left:208px;top:18px;display:flex;align-items:center;gap:8px;font-size:22px;font-weight:700;color:var(--blue-dark)}
.brand .dot{width:34px;height:34px;border-radius:50%;background:var(--blue-dark)}
.header .phone{position:absolute;left:700px;top:29px;display:flex;align-items:center;gap:8px;font:700 19px Roboto,Arial,sans-serif;color:var(--ink);white-space:nowrap}
.header .book{left:882px;top:23px;height:36px;padding:0 22px}

.nav{top:83px;height:37px;background:#111}
.nav ul{position:absolute;left:210px;top:0;display:flex;list-style:none;height:37px}
.nav a{display:block;line-height:37px;padding:0 16px;font-size:11px;font-weight:500;color:var(--white);text-decoration:none;text-transform:uppercase}
.nav li.active a{background:var(--green)}
.nav .search{position:absolute;left:832px;top:8px;width:156px;height:22px;border-radius:11px;background:var(--white);font-size:10px;color:#999;padding:4px 12px}
.nav .search svg{position:absolute;right:8px;top:5px}

/* hero */
.hero{top:120px;height:472px;background:linear-gradient(180deg,#1d80c9 0%,#6fb8e3 45%,#cfe6c2 62%,#5aa52b 72%,#2f7a13 100%)}
.hero h1{position:absolute;left:208px;top:140px;font-size:27px;font-weight:700;color:var(--white)}
.hero h1 span{color:var(--ink)}
.hero p{position:absolute;left:208px;top:194px;width:440px;font-size:14px;line-height:1.5;color:#1d2e3d}
.hero .btn{top:258px}
.arrow{position:absolute;top:200px;width:38px;height:38px;border-radius:50%;background:rgba(0,0,0,.55);display:flex;align-items:center;justify-content:center}

/* capability */
.capability{top:592px;height:564px;background:linear-gradient(180deg,#2e2e2e,#1f1f1f)}
.cap-col{position:absolute;top:88px}
.cap-col h2{font-size:27px;font-weight:700;line-height:1.1}
.cap-col h3{font-size:19px;font-weight:400;color:var(--white);margin-bottom:34px}
.cap-col ul{list-style:none}
.cap-col li{display:flex;align-items:center;gap:18px;height:60px;font-size:14px;color:var(--white)}
.cap-left{left:208px}.cap-left h2{color:var(--blue)}
.cap-right{left:808px}.cap-right h2{color:var(--green)}
.capability .btn{top:464px}

/* about */
.about{top:1156px;height:410px}
.about h2{position:absolute;left:212px;top:62px;font-size:27px;font-weight:700;color:var(--blue)}
.about h2 span{color:var(--ink)}
.about p{position:absolute;left:212px;width:350px;font-size:12.5px;line-height:1.65}
.video-frame{position:absolute;left:570px;top:66px;width:60px;height:60px;border-left:10px solid var(--blue);border-top:10px solid var(--blue)}
.video{left:590px;top:86px;width:380px;height:238px;background:linear-gradient(135deg,#4a4a4a,#1e1e1e)}
.play{position:absolute;left:748px;top:184px;width:60px;height:60px;border-radius:50%;border:3px solid var(--white);display:flex;align-items:center;justify-content:center}

/* service panels */
.panels{top:1566px;height:400px}
.panel{position:absolute;top:0;width:600px;height:400px;text-align:center;color:var(--white)}
.panel-blue{left:0;background:linear-gradient(135deg,#2a6fb8,#0f4a8c)}
.panel-dark{left:600px;background:linear-gradient(135deg,#3a3a3a,#151515)}
.panel .kicker{margin-top:92px;font-size:12px;font-weight:600}
.panel h2{font-size:27px;font-weight:700;margin:4px 0 22px}
.panel p{width:410px;margin:0 auto;font-size:12px;line-height:1.65}
.panel .btn{left:50%;transform:translateX(-50%);top:296px}

/* computer recycling */
.computer{top:1966px;height:294px;text-align:center}
.computer h2{margin-top:54px;font-size:27px;font-weight:700;color:var(--blue)}
.computer h2 span{color:var(--ink)}
.computer p{width:720px;margin:20px auto 0;font-size:12px;line-height:1.75}
.computer .btn{left:533px;top:210px}

/* certified */
.certified{top:2260px;height:511px;background:var(--light)}
.certified h2{text-align:center;margin-top:60px;font-size:27px;font-weight:700;color:var(--blue)}
.certified h2 span{color:var(--ink)}
.certified p.lead{width:720px;margin:16px auto 0;text-align:center;font-size:12px;line-height:1.7}
.cert{position:absolute;top:176px;width:180px;height:266px}
.cert-note{left:210px;background:var(--blue);color:var(--white);text-align:center;padding:46px 16px 0;font-size:12px;line-height:1.6}
.cert-note .btn{position:static;margin-top:26px;height:30px}
.cert-doc{background:linear-gradient(180deg,#f7f9f4,#c9dcc0);border:3px solid #222}
.cert-doc.plain{background:linear-gradient(180deg,#ffffff,#ececec)}

/* testimonials */
.testimonials{top:2771px;height:527px}
.testimonials h2{text-align:center;margin-top:58px;font-size:27px;font-weight:700;color:var(--blue)}
.quote{position:absolute;top:130px;width:250px;height:288px;background:#eceff2;text-align:center;padding:24px 20px 0}
.quote .mark{width:24px;height:24px;border-radius:50%;background:var(--green);margin:0 auto 14px;display:flex;align-items:center;justify-content:center}
.quote p{font-size:11.5px;line-height:1.75}
.quote .avatar{width:40px;height:40px;border-radius:50%;background:#b8c0c8;margin:18px auto 8px}
.quote h4{font-size:14px;font-weight:500;color:var(--ink)}
.quote small{font-size:10px}
.dots{position:absolute;top:448px;left:0;width:1200px;display:flex;justify-content:center;gap:6px}
.dots i{width:10px;height:10px;border-radius:50%;border:1px solid #aaa}
.dots i.on{background:#aaa}

/* why */
.why-band{top:3298px;height:52px;background:var(--green);text-align:center}
.why-band h2{line-height:52px;font-size:26px;font-weight:700;color:var(--white)}
.why{top:3350px;height:273px;background:linear-gradient(180deg,#fff,#f0f0f0)}
.feature{position:absolute;top:70px;width:230px;text-align:center}
.feature h3{margin-top:12px;font-size:15px;font-weight:700;color:var(--ink)}
.feature p{margin-top:10px;font-size:11.5px;line-height:1.7}

/* footer */
.footer{top:3623px;height:273px;background:#161616;color:#ccc}
.footer h4{font-size:12px;font-weight:700;color:var(--white);margin-bottom:14px}
.fcol{position:absolute;top:44px;font-size:11.5px;line-height:1.7}
.fcol ul{list-style:none}
.footer .copy{position:absolute;left:208px;top:226px;font-size:11px}
.footer-brand{position:absolute;left:818px;top:0;width:382px;height:273px;background:var(--blue)}
.footer-brand .brand{left:20px;top:38px;color:var(--white)}
.footer-brand .brand .dot{background:var(--white)}
.social{position:absolute;left:76px;top:88px;display:flex;gap:6px}
.social i{width:18px;height:18px;background:var(--white)}
.contact-tab{position:absolute;left:54px;top:248px;width:110px;height:25px;background:var(--white);color:var(--ink);font:700 11px Roboto,Arial,sans-serif;display:flex;align-items:center;justify-content:center}
</style>
</head>
<body>

<header class="section header">
  <div class="brand"><span class="dot"></span>Velno Recycling</div>
  <div class="phone">
    <svg width="18" height="18" viewBox="0 0 24 24"><path fill="#1c6fc4" d="M6.6 10.8a15 15 0 0 0 6.6 6.6l2.2-2.2a1 1 0 0 1 1-.25 11.4 11.4 0 0 0 3.6.57 1 1 0 0 1 1 1V20a1 1 0 0 1-1 1A17 17 0 0 1 3 4a1 1 0 0 1 1-1h3.5a1 1 0 0 1 1 1c0 1.25.2 2.45.57 3.57a1 1 0 0 1-.25 1z"/></svg>
    (512) 555-0142
  </div>
  <a class="btn btn-green book">Book Online</a>
</header>

<nav class="section nav">
  <ul>
    <li class="active"><a>Home</a></li>
    <li><a>About</a></li>
    <li><a>Services</a></li>
    <li><a>Certifications</a></li>
    <li><a>News</a></li>
    <li><a>Contact</a></li>
  </ul>
  <div class="search">Search
    <svg width="12" height="12" viewBox="0 0 24 24"><circle cx="10" cy="10" r="7" fill="none" stroke="#333" stroke-width="3"/><path d="M15 15l6 6" stroke="#333" stroke-width="3"/></svg>
  </div>
</nav>

<section class="section hero" role="img" aria-label="Recycling bin full of electronics and a stack of laptops on a green field under a blue sky">
  <a class="arrow" style="left:76px"><svg width="12" height="12" viewBox="0 0 12 12"><path d="M8 1L3 6l5 5" fill="none" stroke="#fff" stroke-width="2"/></svg></a>
  <a class="arrow" style="left:1086px"><svg width="12" height="12" viewBox="0 0 12 12"><path d="M4 1l5 5-5 5" fill="none" stroke="#fff" stroke-width="2"/></svg></a>
  <h1>Recycling Today <span>Reuse Tomorrow</span></h1>
  <p>We resell and recycling electronics such as laptops, computer components, Tovlets, Brunos, etc.</p>
  <a class="btn btn-blue" style="left:208px">Schedule A Pickup</a>
  <a class="btn btn-green" style="left:366px">Call (512) 555-0142</a>
</section>

<section class="section capability">
  <div class="cap-col cap-left">
    <h2>Capability</h2>
    <h3>Overview</h3>
    <ul>
      <li><svg width="22" height="22" viewBox="0 0 24 24" fill="none" stroke="#1c6fc4" stroke-width="2"><rect x="2" y="7" width="12" height="9"/><path d="M14 10h4l3 3v3h-7"/><circle cx="6" cy="18" r="2"/><circle cx="17" cy="18" r="2"/></svg>Logistics</li>
      <li><svg width="22" height="22" viewBox="0 0 24 24" fill="none" stroke="#1c6fc4" stroke-width="2"><path d="M12 3l4 6H8zM4 18l4-6 3 5zM20 18h-7l3-6z"/></svg>Recycling</li>
      <li><svg width="22" height="22" viewBox="0 0 24 24" fill="none" stroke="#1c6fc4" stroke-width="2"><rect x="3" y="4" width="18" height="14"/><path d="M7 9h10M7 13h6"/></svg>Certificates</li>
      <li><svg width="22" height="22" viewBox="0 0 24 24" fill="none" stroke="#1c6fc4" stroke-width="2"><path d="M9 5L4 10l5 5"/><path d="M4 10h10a6 6 0 0 1 0 12"/></svg>Returns</li>
    </ul>
  </div>
  <div class="ph" role="img" aria-label="Recycling bin filled with discarded devices" style="left:494px;top:32px;width:210px;height:404px;background:radial-gradient(ellipse at 50% 55%,#5c6a5a,#2a2a2a 70%)"></div>
  <div class="cap-col cap-right">
    <h2>Recycling</h2>
    <h3>Products</h3>
    <ul>
      <li><svg width="22" height="22" viewBox="0 0 24 24" fill="none" stroke="#2fb10f" stroke-width="2"><rect x="3" y="4" width="18" height="12"/><path d="M8 20h8M12 16v4"/></svg>Computer</li>
      <li><svg width="22" height="22" viewBox="0 0 24 24" fill="none" stroke="#2fb10f" stroke-width="2"><rect x="5" y="5" width="14" height="10"/><path d="M2 19h20"/></svg>Laptops</li>
      <li><svg width="22" height="22" viewBox="0 0 24 24" fill="none" stroke="#2fb10f" stroke-width="2"><rect x="5" y="3" width="14" height="18" rx="2"/></svg>Tovlets</li>
      <li><svg width="22" height="22" viewBox="0 0 24 24" fill="none" stroke="#2fb10f" stroke-width="2"><rect x="2" y="4" width="20" height="13"/><path d="M8 21h8"/></svg>Brunos</li>
    </ul>
  </div>
  <a class="btn btn-blue" style="left:446px">Schedule A Pickup</a>
  <a class="btn btn-green" style="left:604px">Call (512) 555-0142</a>
</section>

<section class="section about">
  <h2>About <span>Velno Recycling</span></h2>
  <p style="top:112px">At Velno Recycling, we're committed to providing environmentally friendly recycling solutions to Austin and the surrounding areas.</p>
  <p style="top:188px">Founded in 2008, our mission is to process your materials in a safe, non-hazardous manner – with an aim to keep the world environmentally clean. As a certified recycling center, we believe in promoting smart recycling habits in order to achieve long-lasting results.</p>
  <a class="btn btn-blue" style="left:212px;top:300px;height:30px">Find Out More</a>
  <div class="video-frame"></div>
  <div class="ph video" role="img" aria-label="Video still of a hand touching a recycle, reuse, reduce screen"></div>
  <div class="play"><svg width="20" height="22" viewBox="0 0 20 22"><path d="M3 1l16 10L3 21z" fill="#fff"/></svg></div>
</section>

<section class="section panels">
  <div class="panel panel-blue" role="img" aria-label="Blue-tinted photo of electronic waste bins">
    <div class="kicker">Environmentally Friendly</div>
    <h2>Electronic Recycling</h2>
    <p>At Velno Recycling, we strive to keep the environment clean through our wide range of services. Our E-Waste Recycling services were designed to simplify the recycling process for residents in the Austin area. Contact us today and see how you can contribute to making it a world a cleaner place.</p>
    <a class="btn btn-white">Schedule A Pickup</a>
  </div>
  <div class="panel panel-dark" role="img" aria-label="Dark-tinted photo of a recycling pickup crew">
    <div class="kicker">We Come To You</div>
    <h2>Recycling Pickup</h2>
    <p>At Velno Recycling, we go out of our way to make sure your recycling process is made easy as possible. Our Recycling Pickup service is designed to simplify all of your recycling needs. Take a look at all the services we offer and get in touch to see how you can start the process today!</p>
    <a class="btn btn-white">Schedule A Pickup</a>
  </div>
</section>

<section class="section computer">
  <h2>Computer Recycling <span>Made Easy</span></h2>
  <p>Want to make a difference to our environment and planet? Velno Recycling is here to help! Velno Recycling has been helping keep the environment healthy since 2006. We specialize in recycling services that help citizens become experts at reducing waste. We have a passion to keep our world clean and are here to guide you through all the stages of the recycling process.</p>
  <a class="btn btn-blue">Find Out More</a>
</section>

<section class="section certified">
  <h2>Certified <span>Recyclers</span></h2>
  <p class="lead">Processing of electronic assets and electronic scrap, all associated site operations and maintenance, as well as the supporting financial and administrative functions related to these activities and operations.</p>
  <div class="cert cert-note">Has been assessed by Keston Registrar and found to be in compliance with the following Environmental Management Standard: ISO 14001:2015<br><a class="btn btn-white">Full View</a></div>
  <div class="cert cert-doc" style="left:408px" role="img" aria-label="Certificate of registration"></div>
  <div class="cert cert-doc" style="left:605px" role="img" aria-label="Certificate of registration"></div>
  <div class="cert cert-doc plain" style="left:800px" role="img" aria-label="State environmental quality registration letter"></div>
</section>

<section class="section testimonials">
  <h2>Testimonials</h2>
  <div class="quote" style="left:213px">
    <div class="mark"><svg width="12" height="10" viewBox="0 0 12 10"><path d="M0 10V5l3-5h2L3 5h2v5zM7 10V5l3-5h2l-2 5h2v5z" fill="#fff"/></svg></div>
    <p>" Quick pickup, clear paperwork and friendly staff. Our old office laptops were handled with care and every drive was wiped before resale. We will gladly use them again. "</p>
    <div class="avatar" role="img" aria-label="Customer portrait"></div>
    <h4>Marcus Hale</h4><small>Office manager, Austin</small>
  </div>
  <div class="quote" style="left:475px">
    <div class="mark"><svg width="12" height="10" viewBox="0 0 12 10"><path d="M0 10V5l3-5h2L3 5h2v5zM7 10V5l3-5h2l-2 5h2v5z" fill="#fff"/></svg></div>
    <p>" The team made recycling our servers simple. They arrived on time, sorted every part and sent a full report the next day. Great service at a fair price overall. "</p>
    <div class="avatar" role="img" aria-label="Customer portrait"></div>
    <h4>Owen Pratt</h4><small>IT lead, Round Rock</small>
  </div>
  <div class="quote" style="left:737px">
    <div class="mark"><svg width="12" height="10" viewBox="0 0 12 10"><path d="M0 10V5l3-5h2L3 5h2v5zM7 10V5l3-5h2l-2 5h2v5z" fill="#fff"/></svg></div>
    <p>" I dropped off a box of old phones and tablets and felt good knowing they would be reused. Honest people who truly care about keeping our city clean. "</p>
    <div class="avatar" role="img" aria-label="Customer portrait"></div>
    <h4>Nadia Karim</h4><small>Resident, Austin</small>
  </div>
  <div class="dots"><i class="on"></i><i></i><i></i><i></i><i></i></div>
</section>

<section class="section why-band"><h2>Why Choose Velno Recycling</h2></section>
<section class="section why">
  <div class="feature" style="left:225px">
    <svg width="40" height="40" viewBox="0 0 40 40" fill="none" stroke="#333" stroke-width="2"><circle cx="20" cy="14" r="8"/><path d="M17 14h6M20 10v8"/><path d="M6 30h28v6H6z"/></svg>
    <h3>Best Price</h3>
    <p>We pay fair rates for usable devices and keep every fee simple, clear and upfront.</p>
  </div>
  <div class="feature" style="left:485px">
    <svg width="40" height="40" viewBox="0 0 40 40" fill="none" stroke="#333" stroke-width="2"><path d="M10 10h20l-2 26H12z"/><path d="M7 10h26M16 6h8"/><path d="M17 20l3 3 4-5"/></svg>
    <h3>Best Services</h3>
    <p>From pickup to data wiping, our team handles each step with care and fast response.</p>
  </div>
  <div class="feature" style="left:745px">
    <svg width="40" height="40" viewBox="0 0 40 40" fill="none" stroke="#333" stroke-width="2"><circle cx="20" cy="20" r="16"/><path d="M13 21l5 5 9-11"/></svg>
    <h3>Guaranteed</h3>
    <p>Every job is certified and documented, so you know your items were recycled right.</p>
  </div>
</section>

<footer class="section footer">
  <div class="fcol" style="left:208px">
    <h4>CONTACT INFO</h4>
    1420 Maple Ridge Dr<br>Austin TX 78700<br><br>(512) 555-0142<br>hello@velnorecycling.com
  </div>
  <div class="fcol" style="left:442px">
    <h4>QUICK LINKS</h4>
    <ul><li>Home</li><li>About</li><li>Services</li><li>Certifications</li><li>News</li><li>Contact</li></ul>
  </div>
  <div class="fcol" style="left:603px">
    <h4>HELPFUL LINKS</h4>
    <ul><li>Service Area</li><li>News</li><li>Terms of Use</li><li>Privacy Policy</li><li>Sitemap</li></ul>
  </div>
  <div class="copy">©2018 by Velno Recycling. All Rights Reserved.</div>
  <div class="footer-brand">
    <div class="brand"><span class="dot"></span>Velno Recycling</div>
    <div class="social"><i></i><i></i><i></i></div>
    <div class="contact-tab">CONTACT US</div>
  </div>
</footer>

</body>
</html>
```